"Brightly Bold Sisters" book

I am self-publishing a legal guide for women, which will give them information about their rights and how to navigate the legal world in an easy-to-read style. I'd like to see a design using the colours in the logo I've also had designed for the brand by the same name. Then I can provide the winner my photo and a blurb for the back cover. I am the author: Melda Strovik.

Font styles to use
Serif

Requirements
Must have
• Casual but trustworthy feel. Not too formal - it's not a legal text book.
• Back cover must have my photo, a space for the blurb, and a space for the barcode
Nice to have
• Abstract - not my photo on the front, and not a bunch of smiling women either.

```html
<!DOCTYPE html>
<html lang="en">
<head>
<meta charset="utf-8">
<title>Brightly Bold Sisters — Book Jacket</title>
<link rel="stylesheet" href="https://fonts.googleapis.com/css2?family=Amatic+SC:wght@700&family=Josefin+Sans:wght@300;400&display=swap">
<style>
  :root {
    --backdrop: #ebebec;
    --cover-orange: #e4521f;
    --spine-orange: #dc4b1b;
    --spine-edge: #c8421a;
    --ink: #1d1a19;
    --paper-white: #fbf7f3;
    --figure-light: #f1eeeb;
    --figure-mid: #d8d3ce;
  }
  html, body {
    margin: 0;
    width: 1200px;
    height: 927px;
    overflow: hidden;
    background: var(--backdrop);
  }
  .canvas {
    position: relative;
    width: 1200px;
    height: 927px;
  }
  .book {
    position: absolute;
    left: 285px;
    top: 40px;
    width: 630px;
    height: 847px;
    display: flex;
    box-shadow: 0 18px 40px rgba(0,0,0,0.18);
    border-radius: 4px;
    overflow: hidden;
  }

  /* Spine */
  .spine {
    position: relative;
    width: 90px;
    height: 100%;
    background: var(--spine-orange);
    border-right: 2px solid var(--spine-edge);
    box-sizing: border-box;
  }
  .spine-emblem {
    position: absolute;
    left: 27px;
    top: 28px;
    width: 36px;
    height: 80px;
  }
  .spine-title {
    position: absolute;
    left: 50%;
    top: 140px;
    transform: translateX(-50%);
    margin: 0;
    writing-mode: vertical-rl;
    font-family: "Amatic SC", "Comic Sans MS", cursive;
    font-weight: 700;
    font-size: 46px;
    letter-spacing: 4px;
    line-height: 1;
    color: var(--ink);
    text-transform: uppercase;
    white-space: nowrap;
  }
  .spine-author {
    position: absolute;
    left: 50%;
    bottom: 60px;
    transform: translateX(-50%);
    margin: 0;
    writing-mode: vertical-rl;
    font-family: "Josefin Sans", "Helvetica Neue", sans-serif;
    font-weight: 300;
    font-size: 24px;
    letter-spacing: 2px;
    line-height: 1;
    color: var(--paper-white);
    text-transform: uppercase;
    white-space: nowrap;
  }

  /* Front cover */
  .front-cover {
    position: relative;
    flex: 1;
    height: 100%;
    background: var(--cover-orange);
  }
  .book-title {
    margin: 0;
    position: absolute;
    left: 56px;
    top: 50px;
    width: 440px;
    font-family: "Amatic SC", "Comic Sans MS", cursive;
    font-weight: 700;
    color: var(--ink);
    line-height: 0.9;
    text-transform: uppercase;
  }
  .book-title span { display: block; }
  .title-line-1 {
    font-size: 92px;
    letter-spacing: 4px;
    transform: rotate(-4deg);
    transform-origin: left bottom;
  }
  .title-line-2 {
    font-size: 150px;
    letter-spacing: 6px;
    margin-left: 36px;
  }
  .title-line-3 {
    font-size: 100px;
    letter-spacing: 8px;
    margin-left: 56px;
  }
  .scales-illustration {
    position: absolute;
    left: 78px;
    top: 440px;
    width: 384px;
    height: 260px;
  }
  .author-name {
    position: absolute;
    right: 48px;
    bottom: 84px;
    margin: 0;
    font-family: "Josefin Sans", "Helvetica Neue", sans-serif;
    font-weight: 300;
    font-size: 34px;
    letter-spacing: 2px;
    color: var(--paper-white);
    text-transform: uppercase;
  }
</style>
</head>
<body>
  <main class="canvas">
    <article class="book">
      <aside class="spine">
        <svg class="spine-emblem" viewBox="0 0 36 80" role="img"
             aria-label="Small scales of justice emblem with two standing women">
          <rect x="0" y="0" width="36" height="80" rx="4" fill="var(--figure-light)" opacity="0.9"/>
        </svg>
        <p class="spine-title">Brightly Bold Sisters</p>
        <p class="spine-author">Melda Strovik</p>
      </aside>

      <section class="front-cover">
        <h1 class="book-title">
          <span class="title-line-1">Brightly</span>
          <span class="title-line-2">Bold</span>
          <span class="title-line-3">Sisters</span>
        </h1>

        <svg class="scales-illustration" viewBox="0 0 384 260" role="img"
             aria-label="Illustration: scales of justice with a classical column at the centre and two women standing on the hanging pans">
          <defs>
            <linearGradient id="illustration-tone" x1="0" y1="0" x2="0" y2="1">
              <stop offset="0" stop-color="var(--figure-light)"/>
              <stop offset="1" stop-color="var(--figure-mid)"/>
            </linearGradient>
          </defs>
          <rect x="0" y="0" width="384" height="260" rx="10" fill="url(#illustration-tone)" opacity="0.9"/>
        </svg>

        <p class="author-name">Melda Strovik</p>
      </section>
    </article>
  </main>
</body>
</html>
```